Redesign of business card for Birchline Mechanical

We are looking for a new design for our business cards for Birchline Mechanical. We are a plumbing & HVAC construction company, operating on the West Coast of Canada and USA. Logo attached.
Industry/Entity Type
Construction - Plumbing & HVAC
Contact Information for Business Card
Name, address, phone numbers, email, website address
Look and feel
Each slider illustrates characteristics of the customer's brand and the style your logo design should communicate.

```html
<!DOCTYPE html>
<html lang="en">
<head>
<meta charset="utf-8">
<title>Birchline Mechanical – Business Card</title>
<link rel="stylesheet" href="https://fonts.googleapis.com/css2?family=Roboto:wght@400&family=Roboto+Condensed:wght@500;700&display=swap">
<style>
  :root {
    --backdrop: #d6d6d6;
    --ink: #000000;
    --paper: #f4f4f4;
    --steel: #7a7a7a;
    --charcoal: #303030;
    --white: #ffffff;
  }
  * { margin: 0; padding: 0; box-sizing: border-box; }
  html, body { width: 1200px; height: 1040px; overflow: hidden; }
  body { background: var(--backdrop); position: relative; font-family: "Roboto", Arial, sans-serif; }

  .card {
    position: absolute;
    border-radius: 16px;
    overflow: hidden;
  }
  .card--front { left: 285px; top: 130px; width: 641px; height: 366px; background: var(--ink); }
  .card--back  { left: 285px; top: 568px; width: 645px; height: 368px; background: var(--charcoal); }

  .card__shape { position: absolute; inset: 0; width: 100%; height: 100%; }

  .contact { position: absolute; left: 34px; top: 76px; color: var(--white); }
  .contact__name { font-family: "Roboto Condensed", Arial, sans-serif; font-weight: 700; font-size: 25px; line-height: 1; }
  .contact__title { font-size: 15px; margin-top: 5px; }
  .contact__address { font-size: 15.5px; line-height: 20px; margin-top: 36px; }
  .contact__list { list-style: none; margin-top: 18px; font-size: 15.5px; line-height: 20px; }
  .contact__list li { display: flex; align-items: center; gap: 9px; }
  .contact__list svg { width: 13px; height: 13px; flex: none; margin-left: 1px; }

  .wordmark {
    position: absolute;
    display: flex; align-items: center;
    font-family: "Roboto Condensed", Arial, sans-serif;
    font-weight: 500;
    text-transform: uppercase;
    letter-spacing: 0.5px;
    white-space: nowrap;
  }
  .wordmark__square { flex: none; }
  .wordmark--front { left: 400px; top: 168px; font-size: 20px; color: var(--ink); gap: 8px; }
  .wordmark--front .wordmark__square { width: 16px; height: 16px; background: var(--ink); }
  .wordmark--back { left: 50%; top: 50%; transform: translate(-50%, -50%); font-size: 38px; color: var(--white); gap: 14px; }
  .wordmark--back .wordmark__square { width: 30px; height: 30px; background: var(--white); }
</style>
</head>
<body>

<section class="card card--front" aria-label="Business card front">
  <svg class="card__shape" viewBox="0 0 641 366" preserveAspectRatio="none" aria-hidden="true">
    <path d="M468 0 L318 150 Q300 178 318 206 L458 366 L641 366 L641 0 Z" fill="var(--steel)"/>
    <path d="M482 0 L333 150 Q315 178 333 206 L473 366 L641 366 L641 0 Z" fill="var(--paper)"/>
  </svg>

  <div class="contact">
    <h1 class="contact__name">Owen Harlow</h1>
    <p class="contact__title">President</p>
    <p class="contact__address">2170 Cedarcrest Lane<br>Lakemont, NY 11350</p>
    <ul class="contact__list">
      <li>
        <svg viewBox="0 0 24 24"><path fill="#fff" d="M6.6 10.8a15.1 15.1 0 0 0 6.6 6.6l2.2-2.2c.3-.3.7-.4 1-.2 1.1.4 2.3.6 3.6.6.6 0 1 .4 1 1V20c0 .6-.4 1-1 1C10.6 21 3 13.4 3 4c0-.6.4-1 1-1h3.5c.6 0 1 .4 1 1 0 1.3.2 2.5.6 3.6.1.3 0 .7-.2 1z"/></svg>
        <span>(604) 5521-8837</span>
      </li>
      <li>
        <svg viewBox="0 0 24 24"><rect x="2" y="5" width="20" height="14" fill="#fff"/><path d="M2 5l10 8 10-8" fill="none" stroke="#000" stroke-width="1.8"/></svg>
        <span>name@birchlinemechanical.com</span>
      </li>
      <li>
        <svg viewBox="0 0 24 24"><circle cx="12" cy="12" r="10" fill="#fff"/><path d="M8 7c2 1 1 3 3 4s0 3 1 5M15 5c-1 2 1 3 3 3" fill="none" stroke="#000" stroke-width="1.8"/></svg>
        <span>www.birchlinemechanical.com</span>
      </li>
    </ul>
  </div>

  <div class="wordmark wordmark--front">
    <span class="wordmark__square" aria-hidden="true"></span>
    <span>Birchline Mechanical</span>
  </div>
</section>

<section class="card card--back" aria-label="Business card back">
  <div class="wordmark wordmark--back">
    <span class="wordmark__square" aria-hidden="true"></span>
    <span>Birchline Mechanical</span>
  </div>
</section>

</body>
</html>
```